Local Roofing/Construction company business needs new biz card design

We need a new business card design, current cards are from the start of this operation and generic at best. We are a local Construction Company (General Contractor) with a majority of our work originating from insurance claims-exterior finish work is the main focus (Roofs-Siding-Gutters etc). Heavily involved with homeowners and the low ball offers they receive from insurance company's after a insurable event takes place. I have attached some of our original logo file(s) below.

```html
<!DOCTYPE html>
<html lang="en">
<head>
<meta charset="utf-8">
<title>Ironvale Builders – Business Card</title>
<link rel="stylesheet" href="https://fonts.googleapis.com/css2?family=Krona+One&family=Poppins:wght@400;700&display=swap">
<style>
  :root {
    --backdrop: #d3d4d6;
    --brand-green: #65b874;
    --brand-green-deep: #5aae69;
    --paper: #ffffff;
    --ink: #2a2a2a;
  }
  * { box-sizing: border-box; margin: 0; padding: 0; }
  html, body { width: 900px; height: 1200px; overflow: hidden; }
  body {
    background: var(--backdrop);
    position: relative;
    font-family: "Poppins", sans-serif;
    color: var(--ink);
  }
  .card {
    position: absolute;
    left: 135px;
    width: 630px;
    height: 358px;
  }
  .card--front { top: 214px; }
  .card--back { top: 628px; background: var(--paper); }

  .front-pattern {
    position: absolute; inset: 0;
    background: linear-gradient(135deg, var(--brand-green) 0%, var(--brand-green-deep) 100%);
  }
  .front-brand {
    position: absolute; inset: 0;
    display: flex; align-items: center; justify-content: center; gap: 16px;
  }
  .front-brand__square {
    width: 34px; height: 34px; background: var(--paper);
  }
  .front-brand__name {
    font-family: "Poppins", sans-serif;
    font-weight: 700;
    font-size: 44px;
    letter-spacing: 0.5px;
    color: var(--paper);
    text-transform: uppercase;
  }

  .back-brand {
    position: absolute;
    left: 137px; top: 103px;
    width: 152px; height: 154px;
    display: flex; flex-direction: column; align-items: center; justify-content: center; gap: 14px;
  }
  .back-brand__square { width: 40px; height: 40px; background: var(--brand-green); }
  .back-brand__name {
    font-family: "Poppins", sans-serif;
    font-weight: 700;
    font-size: 22px;
    line-height: 1.1;
    text-align: center;
    text-transform: uppercase;
    color: var(--brand-green);
  }
  .divider {
    position: absolute;
    left: 315px; top: 103px;
    width: 1px; height: 153px;
    background: var(--ink);
  }
  .person {
    position: absolute;
    left: 340px; top: 100px;
  }
  .person__name {
    font-family: "Krona One", sans-serif;
    font-size: 17px;
    letter-spacing: 0.6px;
    color: var(--brand-green);
    text-transform: uppercase;
    line-height: 1.2;
  }
  .person__title {
    font-size: 14px;
    letter-spacing: 0.6px;
    margin-top: 2px;
  }
  .contacts {
    position: absolute;
    left: 340px; top: 164px;
    list-style: none;
  }
  .contacts li {
    display: flex; align-items: center; gap: 4px;
    height: 24.5px;
    font-size: 14px;
    letter-spacing: 0.3px;
  }
  .contacts .phone { letter-spacing: 3px; }
  .contacts svg { width: 13px; height: 13px; flex: none; fill: var(--brand-green); }
</style>
</head>
<body>

  <section class="card card--front">
    <div class="front-pattern" role="img" aria-label="Repeating tiled pattern of the company mark in darker green"></div>
    <div class="front-brand">
      <span class="front-brand__square"></span>
      <span class="front-brand__name">Ironvale Builders</span>
    </div>
  </section>

  <section class="card card--back">
    <div class="back-brand">
      <span class="back-brand__square"></span>
      <span class="back-brand__name">Ironvale<br>Builders</span>
    </div>
    <div class="divider"></div>

    <div class="person">
      <h1 class="person__name">Dalton J Reyes</h1>
      <p class="person__title">Chief Executive Officer</p>
    </div>

    <ul class="contacts">
      <li>
        <svg viewBox="0 0 24 24"><path d="M6.6 10.8a15.1 15.1 0 0 0 6.6 6.6l2.2-2.2a1 1 0 0 1 1-.25 11.4 11.4 0 0 0 3.6.57 1 1 0 0 1 1 1V20a1 1 0 0 1-1 1A17 17 0 0 1 3 4a1 1 0 0 1 1-1h3.5a1 1 0 0 1 1 1c0 1.25.2 2.45.57 3.6a1 1 0 0 1-.25 1z"/></svg>
        <span class="phone">555-210-4837</span>
      </li>
      <li>
        <svg viewBox="0 0 24 24"><path d="M7 1h10a2 2 0 0 1 2 2v18a2 2 0 0 1-2 2H7a2 2 0 0 1-2-2V3a2 2 0 0 1 2-2zm0 3v15h10V4zm5 16.2a1 1 0 1 0 0 2 1 1 0 0 0 0-2z"/></svg>
        <span class="phone">555-384-9126</span>
      </li>
      <li>
        <svg viewBox="0 0 24 24"><path d="M2 5h20v14H2zm2 2v.5l8 5 8-5V7zm0 2.8V17h16V9.8l-8 5z"/></svg>
        <span>info@ironvalebuilders.com</span>
      </li>
      <li>
        <svg viewBox="0 0 24 24"><path d="M12 2a10 10 0 1 0 0 20 10 10 0 0 0 0-20zm6.9 9h-3a15 15 0 0 0-1.3-5.6A8 8 0 0 1 18.9 11zM12 4c.9 1.2 1.8 3.7 1.9 7h-3.8c.1-3.3 1-5.8 1.9-7zM9.4 5.4A15 15 0 0 0 8.1 11h-3a8 8 0 0 1 4.3-5.6zM5.1 13h3a15 15 0 0 0 1.3 5.6A8 8 0 0 1 5.1 13zm6.9 7c-.9-1.2-1.8-3.7-1.9-7h3.8c-.1 3.3-1 5.8-1.9 7zm2.6-1.4a15 15 0 0 0 1.3-5.6h3a8 8 0 0 1-4.3 5.6z"/></svg>
        <span>ironvalebuilders.com</span>
      </li>
    </ul>
  </section>

</body>
</html>
```